wedding DJ & Lighting entertainment

We are a DJ and Lighting production company. We specialize mainly in wedding entertainment. I've attached my old postcard in the image folder, however, i would like something new and updated. You can use the same bullet points from the front page, but i would like to have a cleaner look on the front. I'd like to have one large image on the front side and smaller images on the back side. I'd also like to have some text below the logo. I'd like it to say DJ * Lighting * Audio/Visual. I'd also like to have the phrase "Celebrate with Style"

Target Market(s)

weddings, private events, women

Industry/Entity Type

It Company

Font styles to use
Sans Serif
Script

Requirements
Must have
• look elegant, sophisticated. Must have my new logo! My logo is attached as one of the files. It's a headphone logo.

```html
<!DOCTYPE html>
<html lang="en">
<head>
<meta charset="utf-8">
<title>Harborlight Productions – Postcard</title>
<link href="https://fonts.googleapis.com/css2?family=Great+Vibes&family=Lato:ital,wght@0,400;0,700;1,700&display=swap" rel="stylesheet">
<style>
  :root{
    --bg:#2b2b2d;
    --paper:#ffffff;
    --red:#e3121b;
    --red-dark:#b80d14;
    --gray:#5a5a5c;
    --gray-light:#9a9a9c;
    --ink:#1e1e1e;
    --photo-a:#3b2a52;
    --photo-b:#7a5a9a;
  }
  *{box-sizing:border-box;margin:0;padding:0}
  html,body{width:902px;height:1200px;overflow:hidden;background:var(--bg)}
  body{position:relative;font-family:"Lato",sans-serif;color:var(--ink)}
  .card{position:absolute;left:114px;width:672px;background:var(--paper);overflow:hidden;box-shadow:0 4px 14px rgba(0,0,0,.45)}
  .card--front{top:40px;height:524px}
  .card--back{top:640px;height:521px}
  .card__shapes{position:absolute;inset:0}

  /* front */
  .brand{position:absolute;left:48px;top:300px;display:flex;align-items:center;gap:9px}
  .brand__dot{width:11px;height:11px;border-radius:50%;background:var(--red);flex:none}
  .brand__name{font-size:19px;line-height:21px;font-weight:400;color:var(--red);letter-spacing:.4px}
  .services-line{position:absolute;left:26px;top:352px;font-size:15px;font-weight:700;letter-spacing:.3px}
  .features{position:absolute;left:26px;top:378px;list-style:none}
  .features li{font-style:italic;font-weight:700;font-size:13px;height:21.5px;display:flex;align-items:center;gap:14px}
  .features li::before{content:"";width:9px;height:9px;border-radius:50%;background:var(--red);margin-left:2px}
  .headline{position:absolute;left:258px;top:404px;font-family:"Great Vibes",cursive;font-weight:400;font-size:54px;line-height:64px;color:var(--ink);white-space:nowrap}
  .headline em{font-style:normal;color:var(--red)}

  /* back */
  .about-tag{position:absolute;left:0;top:190px;width:215px;height:25px;background:var(--red);color:#fff;font-weight:700;font-size:12.5px;line-height:25px;padding-left:18px;border-radius:0 13px 13px 0;white-space:nowrap}
  .about-body{position:absolute;left:18px;top:224px;width:318px;height:244px;overflow:hidden;font-size:12.5px;line-height:14.8px;text-align:justify}
  .about-body p+p{margin-top:7px}
  .about-body .about-body__lead{width:226px;text-align:left}
  .stamp{position:absolute;left:567px;top:42px;width:91px;height:101px;border:1px solid var(--gray-light)}
  .address-line{position:absolute;left:430px;width:228px;height:1px;background:var(--gray-light)}
  .footer{position:absolute;left:0;right:0;bottom:0;height:52px;background:linear-gradient(var(--red),var(--red-dark));display:flex;align-items:center;gap:18px;padding:0 18px;color:#fff;font-size:11.5px;font-weight:700}
  .footer__item{display:flex;align-items:center;gap:6px;line-height:14px}
  .footer__item svg{width:11px;height:11px;flex:none}
</style>
</head>
<body>

<section class="card card--front">
  <svg class="card__shapes" viewBox="0 0 672 524" width="672" height="524">
    <defs>
      <linearGradient id="photoTone" x1="0" y1="0" x2="1" y2="1">
        <stop offset="0" stop-color="var(--photo-a)"/>
        <stop offset=".55" stop-color="var(--photo-b)"/>
        <stop offset="1" stop-color="var(--photo-a)"/>
      </linearGradient>
      <linearGradient id="redWave" x1="0" y1="0" x2="1" y2="0">
        <stop offset="0" stop-color="#c50d15"/><stop offset=".5" stop-color="#ee2a30"/><stop offset="1" stop-color="#c50d15"/>
      </linearGradient>
    </defs>
    <path role="img" aria-label="Photo of a bride and groom sharing their first dance in a purple-lit reception hall with seated guests" fill="url(#photoTone)" d="M0,0 H672 V290 C560,330 440,330 330,290 C220,250 120,140 0,138 Z"/>
    <path fill="url(#redWave)" d="M0,138 C120,140 220,250 330,290 C440,330 560,330 672,290 V318 C560,365 430,355 320,322 C200,286 100,236 0,240 Z"/>
    <path fill="var(--gray)" d="M0,250 C100,246 200,296 320,332 C430,365 560,378 672,330 V345 C570,395 440,390 320,352 C200,314 100,266 0,268 Z"/>
    <rect x="0" y="495" width="672" height="4" fill="var(--red)"/>
    <rect x="0" y="501" width="672" height="23" fill="var(--gray)"/>
  </svg>

  <div class="brand"><span class="brand__dot"></span><span class="brand__name">Harborlight<br>Productions</span></div>
  <div class="services-line">DJ * Lighting * Audio/Visual</div>
  <ul class="features">
    <li>DJ &amp; Emcee Entertainment</li>
    <li>Customized lighting decor</li>
    <li>Event hosting &amp; coordination</li>
    <li>Helpful Planning Tools</li>
    <li>Personalized service</li>
  </ul>
  <h1 class="headline">Celebrate <em>with Style</em></h1>
</section>

<section class="card card--back">
  <svg class="card__shapes" viewBox="0 0 672 521" width="672" height="521">
    <defs>
      <linearGradient id="partyTone" x1="0" y1="0" x2="1" y2="1">
        <stop offset="0" stop-color="#4a3050"/><stop offset=".6" stop-color="#8a5a6a"/><stop offset="1" stop-color="#3a2a30"/>
      </linearGradient>
      <radialGradient id="crowdPink"><stop offset="0" stop-color="#e0a0c0"/><stop offset="1" stop-color="#a0406a"/></radialGradient>
      <radialGradient id="crowdMono"><stop offset="0" stop-color="#c8c8c8"/><stop offset="1" stop-color="#3a3a3a"/></radialGradient>
    </defs>
    <rect role="img" aria-label="Photo of wedding guests dancing on a crowded dance floor" x="0" y="0" width="345" height="172" fill="url(#partyTone)"/>
    <rect x="0" y="172" width="345" height="4" fill="var(--red)"/>
    <path fill="var(--gray)" d="M336,236 C380,300 400,400 368,469 H388 C420,400 394,295 346,230 Z"/>
    <path fill="var(--red)" d="M322,240 C365,305 385,400 350,469 H368 C400,400 380,300 336,236 Z"/>
    <circle cx="333" cy="64" r="75" fill="#fff"/>
    <circle role="img" aria-label="Photo of guests raising their hands under pink lights" cx="333" cy="64" r="70" fill="url(#crowdPink)"/>
    <circle cx="307" cy="177" r="72" fill="#fff"/>
    <circle role="img" aria-label="Black and white photo of guests dancing and cheering" cx="307" cy="177" r="67" fill="url(#crowdMono)"/>
  </svg>

  <div class="about-tag">About Harborlight Productions</div>
  <div class="about-body">
    <p class="about-body__lead">Harborlight Productions will provide your wedding with superior sound, brilliant lighting and professional DJ entertainment to create a truly memorable experience.</p>
    <p>We know planning your big day can be a little overwhelming. You have to coordinate with so many different people along the way. With our services, we'll make sure you have one less thing to worry about. We've got you covered from the moment you arrive to your final farewell.</p>
    <p>With years of entertainment and production experience, we make sure your occasion comes to life for you and your guests. After all, it's your day, your event and your</p>
  </div>

  <div class="stamp"></div>
  <div class="address-line" style="top:259px"></div>
  <div class="address-line" style="top:297px"></div>
  <div class="address-line" style="top:336px"></div>

  <footer class="footer">
    <div class="footer__item">
      <svg viewBox="0 0 12 12"><path fill="#fff" d="M2.5 0.8l2 2.2-1 1.3c.7 1.5 1.8 2.6 3.3 3.3l1.3-1 2.2 2-1.2 1.9C5 10.3 1.7 7 0.6 2z"/></svg>
      888-555-0192
    </div>
    <div class="footer__item">
      <svg viewBox="0 0 12 12"><path fill="#fff" d="M6 1L0.5 6h1.7v5h3V8h1.6v3h3V6h1.7z"/></svg>
      <span>2210 W. Linden Ave. Suite B<br>Fairmont City, CA 92800</span>
    </div>
    <div class="footer__item">
      <svg viewBox="0 0 12 12"><rect x="0.5" y="2.5" width="11" height="7.5" fill="#fff"/><path d="M0.8 2.8L6 7l5.2-4.2" stroke="#c50d15" fill="none"/></svg>
      harborlightevents@mail.com
    </div>
    <div class="footer__item">
      <svg viewBox="0 0 12 12"><circle cx="6" cy="6" r="5.2" fill="none" stroke="#fff" stroke-width="1.2"/><ellipse cx="6" cy="6" rx="2.2" ry="5.2" fill="none" stroke="#fff"/><path d="M1 6h10" stroke="#fff"/></svg>
      www.harborlightevents.com
    </div>
  </footer>
</section>

</body>
</html>
```